Lawyer health website (wordpress design) to improve well being/health for lawyers

I need a webdesign for personal website called www.plumcounselhub.net. Website will be focused on health/wellness for my profession (lawyers) and other professionals too. Will have a blog on a separate page, a calorie counter on first page, and forums for me to begin topics and users to post. Also want the ability to add and delete information on a consistent basis...especially news articles related to my profession. I will want the homepage to include both health related information - different articles and articles related to the professionl. Need a tab to link my vitaloop site. I like format of www.dailyvigornest.com and www.munchtallyhub.com and www.sourbarrister.com. My website will have a mix of these themes and will not be too sarcastic (sourbarrister) but fun and healthy, a place for other attorneys and professionals to go to support eachother in health and wellness and their profession. Will need these things for the website:

(1) Responsive design (can be viewed on mobile phones, ipads, ect.)
(2)Cross browser support
(3) Custom background and colors
(4) Allow admin to post on front end and to add pages and delete and add info
(5) All post will have social media share
(6)Admin can control what is posted on page so if someone comments admin can review it before its posted on articles...forums no control over that. If admin wants to I can change the review function.
(7) Users can sign in with social media accounts or create a user name and password
(8) I am a female attorney so I prefer it be a bit more feminine but I will encourage males to follow the page as well.
(9) Feature attorney of the month or week on a page. I think this would be cool to do on a separate page highlighting an attorney, their practice area, their fitness goals ect.

Target Market(s)

Attorneys

Industry/Entity Type

Health

Coding

Coded - Design and coding required

Number of Pages Required

5+ page

Font styles to use
Serif

Colors
cadf82
85cae6
0355a3
00a990

Requirements
Must have
• Home page with "Featured attorney" section in a corner of page so users can click on that pic to learn about that "Feautured attorney" and how he/she stays fit. Also, calorie counter on home page, blog, Contact Us Page, and Forum Page.
• I MUST HAVE ABILITY TO ADD/DELETE CONTENT ON MY WEBSITE ON A CONSISTENT BASIS.

```html
<!DOCTYPE html>
<html lang="en">
<head>
<meta charset="utf-8">
<title>PlumCounselHub – Health &amp; Wellness for Lawyers</title>
<link href="https://fonts.googleapis.com/css2?family=Open+Sans:wght@400;600;700&family=Merriweather:wght@400;700&display=swap" rel="stylesheet">
<style>
:root{
  --teal:#00a990;
  --sky:#2fa4d9;
  --azure:#1f8ed6;
  --navy:#0355a3;
  --mist:#85cae6;
  --lime:#cadf82;
  --calc:#4aa8d8;
  --go:#e8542d;
  --ink:#2b2b2b;
  --text:#6b6b6b;
  --muted:#9a9a9a;
  --rule:#e3e3e3;
  --page:#ffffff;
  --footer:#2a2b2d;
  --footer-deep:#1d1e20;
  --footer-text:#a9acb0;
  --serif:"Merriweather",Georgia,serif;
}
*{box-sizing:border-box;margin:0;padding:0}
html,body{width:1200px;height:2636px;overflow:hidden}
body{position:relative;background:var(--page);font-family:"Open Sans",Arial,sans-serif;color:var(--text);font-size:13px;line-height:1.55}
.abs{position:absolute}
a{color:inherit;text-decoration:none}

/* header */
.site-header{left:0;top:0;width:1200px;height:112px;background:#fff;border-bottom:4px solid var(--lime)}
.brand{left:100px;top:34px;display:flex;align-items:center;gap:12px}
.brand-dot{width:34px;height:34px;border-radius:50%;background:var(--teal)}
.brand-name{font-family:var(--serif);font-size:24px;font-weight:700;color:var(--ink)}
.main-nav{right:100px;top:30px;display:flex;gap:4px}
.main-nav a{font-size:13px;color:var(--text);padding:14px 18px}
.main-nav a.active{background:var(--teal);color:#fff}

/* hero */
.hero{left:0;top:112px;width:1200px;height:708px;background:linear-gradient(100deg,#6fa7c9 0%,#a9cfe4 30%,#dcedf5 55%,#c5e0e0 75%,#7fbcb8 100%)}
.hero-title{left:100px;top:150px;font-family:var(--serif);font-weight:700;font-size:40px;color:#fff;letter-spacing:.5px;line-height:1.2}
.hero-sub{left:100px;top:214px;width:540px;color:#fff;font-size:16px;line-height:1.45}

/* feature boxes */
.features{left:100px;top:580px;width:1000px;height:220px;display:flex}
.feature{flex:1;padding:22px 26px;color:#fff}
.feature.teal{background:var(--teal)}
.feature.azure{background:var(--azure)}
.feature.navy{background:var(--navy)}
.feature h3{font-family:var(--serif);font-size:19px;font-weight:700;margin-bottom:12px}
.feature p{font-size:12px;line-height:1.6;opacity:.95}
.btn-more{display:inline-block;margin-top:16px;border:1px solid rgba(255,255,255,.75);padding:5px 14px;font-size:12px}
.featured-row{display:flex;gap:14px;align-items:flex-start}
.featured-photo{flex:none;width:64px;height:64px;border-radius:50%;background:linear-gradient(135deg,var(--mist),#e9d8c8);border:2px solid #fff}
.hours{list-style:none}
.hours li{display:flex;justify-content:space-between;font-size:12px;padding:9px 0;border-bottom:1px solid rgba(255,255,255,.25)}

/* posts */
.post{width:320px}
.date-badge{display:inline-block;background:var(--teal);color:#fff;font-size:11px;font-weight:700;padding:5px 12px}
.post-photo{width:320px;height:230px;margin-top:14px}
.post h2{font-family:var(--serif);font-size:20px;font-weight:700;color:var(--ink);line-height:1.35;margin:18px 0 14px}
.post p{font-size:12px;line-height:1.65}
.post-meta{font-size:11px;color:var(--muted);border-top:1px solid var(--rule);padding-top:8px;margin-top:14px}
.post-meta a{color:var(--teal)}
.show-all{left:680px;top:2050px;font-size:12px;color:var(--ink)}

/* sidebar */
.calorie{left:780px;top:840px;width:320px;height:400px;background:var(--calc);padding:20px 22px;color:#fff}
.calorie h3{font-family:var(--serif);font-size:25px;font-weight:700;line-height:1.3;margin-bottom:18px}
.calorie label{display:block;font-size:13px;margin-bottom:4px}
.field{background:#fff;height:34px;margin-bottom:14px}
.row{display:flex;gap:12px}
.row > div{flex:1}
.select{background:#fff;color:var(--ink);height:34px;padding:7px 10px;font-size:13px;display:flex;justify-content:space-between}
.go{background:var(--go);color:#fff;width:60px;height:34px;text-align:center;line-height:34px;font-weight:700}
.clinics{left:780px;top:1270px;width:320px;list-style:none}
.clinics li{display:flex;justify-content:space-between;font-size:14px;color:var(--text);padding:14px 4px;border-bottom:1px solid var(--rule)}
.clinics li span{color:var(--teal)}
.appointment{left:780px;top:1580px;width:320px}
.appointment h4{font-family:var(--serif);font-size:15px;font-weight:700;color:var(--ink);padding-bottom:10px;border-bottom:2px solid var(--lime);margin-bottom:14px}
.appointment p{font-size:12px;margin-bottom:16px}
.contact-line{display:flex;align-items:center;gap:12px;font-size:12px;padding:9px 0;border-bottom:1px solid var(--rule)}
.contact-line svg{flex:none}
.contact-line b{color:var(--ink)}

/* footer */
.footer-tabs{left:100px;top:2140px;width:1000px;height:80px;display:flex}
.footer-tab{flex:1;padding:12px 22px;color:#fff;position:relative}
.footer-tab.teal{background:var(--teal)}
.footer-tab.azure{background:var(--azure)}
.footer-tab.navy{background:var(--navy)}
.footer-tab h4{font-family:var(--serif);font-size:19px;font-weight:400;line-height:1.5}
.footer-tab p{font-size:11px;opacity:.9}
.footer-tab .arrow{position:absolute;right:20px;top:28px}
.site-footer{left:0;top:2220px;width:1200px;height:380px;background:var(--footer);color:var(--footer-text)}
.footer-col{top:40px;width:300px}
.footer-col h5{font-family:var(--serif);font-size:15px;font-weight:700;color:#fff;margin-bottom:16px;display:flex;justify-content:space-between}
.footer-col p{font-size:12px;line-height:1.7;margin-bottom:14px}
.footer-col ul{list-style:none}
.footer-col li{font-size:12px;margin-bottom:14px;line-height:1.5}
.footer-col li b{display:block;color:#fff;font-weight:600}
.footer-col li small{color:#6f7276;font-size:11px}
.address{display:grid;grid-template-columns:1fr 1.3fr;font-size:12px;line-height:1.7}
.socials{display:flex;gap:8px;margin-top:16px}
.socials span{width:22px;height:22px;background:#44464a}
.bottom-bar{left:0;top:2600px;width:1200px;height:36px;background:var(--footer-deep);color:#6f7276;font-size:11px;padding:10px 100px;display:flex;justify-content:space-between}
</style>
</head>
<body>

<header class="site-header abs">
  <a class="brand abs" href="#"><span class="brand-dot"></span><span class="brand-name">PlumCounselHub</span></a>
  <nav class="main-nav abs">
    <a class="active" href="#">HOME</a><a href="#">MEMBERS</a><a href="#">Some Page</a><a href="#">SOME PAGE 1</a><a href="#">CONTACT</a>
  </nav>
</header>

<section class="hero abs" role="img" aria-label="Slider photo: a smiling woman in a light top enjoying the open sky"></section>
<h1 class="hero-title abs">SOME HEADLINE HERE ( SLIDER)</h1>
<p class="hero-sub abs">Some slider text information, short lorem ipsum text and more information for the reader here.</p>

<section class="features abs">
  <div class="feature teal">
    <h3>Some text heading here</h3>
    <p>Lorem ipsum text comes here, add your content and manage it easily. Lorem ipsum text comes here, add your content.</p>
    <a class="btn-more" href="#">Read more »</a>
  </div>
  <div class="feature azure">
    <h3>Featured Attorney</h3>
    <div class="featured-row">
      <div class="featured-photo" role="img" aria-label="Portrait photo of the featured attorney"></div>
      <p>Meet this month's featured attorney, their practice area and how they stay fit.</p>
    </div>
    <a class="btn-more" href="#">Read more »</a>
  </div>
  <div class="feature navy">
    <h3>Opening Hours</h3>
    <ul class="hours">
      <li><span>Monday - Friday</span><span>8.00 - 17.00</span></li>
      <li><span>Saturday</span><span>9.30 - 15.30</span></li>
      <li><span>Sunday</span><span>9.30 - 15.00</span></li>
    </ul>
  </div>
</section>

<article class="post abs" style="left:100px;top:892px">
  <span class="date-badge">25 FEB 13</span>
  <div class="post-photo" role="img" aria-label="Photo: a family relaxing outdoors on a sunny lawn" style="background:linear-gradient(135deg,#c9a777,#8e7a4f 60%,#6f8a4a)"></div>
  <h2>Study examines methods and procedures for improved diagnosis of pregnancy</h2>
  <p>Maecenas vitae sit amet, consectetur adipiscing elit. Tincidunt volutpat rutrum metus amet sollicitudin interdum. Suspendisse pulvinar, velit vitae pharetra interdum, ante tellus gravida mollis tellus neque nisl elit. Mauris adipiscing mauris fringilla turpis interdum pulvinar nisi malesuada consectetur adipiscing libero non pretium.</p>
  <div class="post-meta">Posted in <a href="#">General</a>, <a href="#">Health</a>, <a href="#">Lifestyle</a></div>
</article>

<article class="post abs" style="left:440px;top:892px">
  <span class="date-badge">25 MAY 13</span>
  <div class="post-photo" role="img" aria-label="Photo: a doctor examining a young patient in a clinic" style="background:linear-gradient(135deg,#eef1f3,#cfd8de 50%,#a9b7c0)"></div>
  <h2>New study links lutein with eye health benefits</h2>
  <p>Maecenas vitae sit amet, consectetur adipiscing elit. Tincidunt volutpat rutrum metus amet sollicitudin interdum. Suspendisse pulvinar, velit vitae pharetra interdum, ante tellus gravida mollis tellus neque nisl elit. Mauris adipiscing mauris fringilla turpis interdum pulvinar nisi malesuada consectetur adipiscing libero non pretium.</p>
  <div class="post-meta">Posted in <a href="#">General</a>, <a href="#">Ophthalmology Clinic</a></div>
</article>

<article class="post abs" style="left:100px;top:1520px">
  <span class="date-badge">30 MAY 13</span>
  <h2>Pets may reduce risk of heart disease</h2>
  <p>Maecenas vitae sit amet, consectetur adipiscing elit. Ut volutpat rutrum metus sit amet sollicitudin. Suspendisse pulvinar, velit vitae pharetra interdum, ante tellus gravida tellus neque nisl elit. Mauris adipiscing mauris.</p>
  <div class="post-meta">Posted in <a href="#">General</a>, <a href="#">Health</a>, <a href="#">Rehabilitation</a></div>
</article>

<article class="post abs" style="left:440px;top:1520px">
  <span class="date-badge">29 MAY 13</span>
  <div class="post-photo" role="img" aria-label="Photo: a stethoscope resting in a doctor's hands" style="height:210px;background:linear-gradient(135deg,#f2eef0,#b56a86 55%,#6d3350)"></div>
  <h2>Mixed results from study of mammogram tool</h2>
  <p>Nulla ullamcorper tincidunt dui sit amet. Duis ipsum ullamcorper ligula lorem, in sagittis quam cursus convallis. Fusce porttitor dui ultrices placerat consectetur. Mauris ipsum neque gravida molestie amet nisl quis nisi.</p>
  <div class="post-meta">Posted in <a href="#">Cardiac Clinic</a>, <a href="#">News</a></div>
</article>

<a class="show-all abs" href="#">Show all »</a>

<aside class="calorie abs">
  <h3>How many calories should you eat?</h3>
  <label>Height</label>
  <div class="field"></div>
  <div class="row">
    <div><label>Weight</label><div class="field"></div></div>
    <div><label>Age</label><div class="field"></div></div>
  </div>
  <label>Gender</label>
  <div class="row">
    <div class="select"><span>Female</span><span>▾</span></div>
    <div class="go" style="flex:none">Go</div>
  </div>
</aside>

<ul class="clinics abs">
  <li>Cardiac Clinic<span>+</span></li>
  <li>Laryngological Clinic<span>+</span></li>
  <li>Ophthalmology Clinic<span>+</span></li>
  <li>Dental Clinic<span>+</span></li>
  <li>Outpatient Rehabilitation<span>+</span></li>
</ul>

<section class="appointment abs">
  <h4>Make An Appointment</h4>
  <p>Lorem ipsum dolor sit amet, consectetur adipiscing elit. Aenean pretium sed quam vel dictum. Nullam a erat sollicitudin lorem.</p>
  <div class="contact-line">
    <svg width="22" height="22" viewBox="0 0 22 22"><circle cx="11" cy="11" r="11" fill="#d9d9d9"/><path d="M8 6l2 3-1.2 1.2a7 7 0 003 3L13 12l3 2-1 2c-4 0-8-4-8-8z" fill="#777"/></svg>
    <span>by phone <b>+1 (555) 014 2276</b></span>
  </div>
  <div class="contact-line">
    <svg width="22" height="22" viewBox="0 0 22 22"><circle cx="11" cy="11" r="11" fill="#d9d9d9"/><rect x="6" y="7.5" width="10" height="7" fill="none" stroke="#777" stroke-width="1.3"/><path d="M6 7.5l5 4 5-4" fill="none" stroke="#777" stroke-width="1.3"/></svg>
    <span>by email <b>care@plumcounselhub.net</b></span>
  </div>
  <div class="contact-line">
    <svg width="22" height="22" viewBox="0 0 22 22"><circle cx="11" cy="11" r="11" fill="#d9d9d9"/><path d="M7 15l1-3 6-6 2 2-6 6z" fill="#777"/></svg>
    <span>or fill in the form on contact page</span>
  </div>
</section>

<section class="footer-tabs abs">
  <div class="footer-tab teal"><h4>Health insurance</h4><p>Text about here, more information</p>
    <svg class="arrow" width="14" height="22" viewBox="0 0 14 22"><path d="M2 2l9 9-9 9" fill="none" stroke="#fff" stroke-width="3"/></svg></div>
  <div class="footer-tab azure"><h4>Medical Records</h4><p>The lab user Medical Records</p>
    <svg class="arrow" width="14" height="22" viewBox="0 0 14 22"><path d="M2 2l9 9-9 9" fill="none" stroke="#fff" stroke-width="3"/></svg></div>
  <div class="footer-tab navy"><h4>Some More Heading</h4><p>Short line of supporting text</p>
    <svg class="arrow" width="14" height="22" viewBox="0 0 14 22"><path d="M2 2l9 9-9 9" fill="none" stroke="#fff" stroke-width="3"/></svg></div>
</section>

<footer class="site-footer abs">
  <div class="footer-col abs" style="left:100px">
    <h5>www.plumcounselhub.net</h5>
    <p>Mauris adipiscing mauris fringilla turpis interdum pulvinar nisi malesuada consectetur.</p>
    <div class="address">
      <span>PlumCounselHub<br>Address 1<br>Address 2<br>City, ST</span>
      <span>+1 (555) 014 2290<br>+1 (555) 014 2291<br>desk@plumcounselhub.net</span>
    </div>
    <div class="socials"><span></span><span></span><span></span><span></span></div>
  </div>
  <div class="footer-col abs" style="left:450px">
    <h5>Latest Posts <span>‹ ›</span></h5>
    <ul>
      <li><b>New study links lutein with eye health benefits</b><small>posted 25 May 2013</small></li>
      <li><b>Pets may reduce risk of heart disease</b><small>posted 30 May 2013</small></li>
      <li><b>Discoveries offer a new explanation for diabetes</b><small>posted 2 June 2013</small></li>
    </ul>
  </div>
  <div class="footer-col abs" style="left:800px">
    <h5>Latest Tweets <span>‹ ›</span></h5>
    <ul>
      <li>Tweets feeds will be displayed here, sample text designed for personal blog<br><small>about 10 hours ago</small></li>
      <li>Tweets feeds will be displayed here, sample text designed for personal blog<br><small>about 12 hours ago</small></li>
      <li>Tweets feeds will be displayed here, sample text designed for personal blog<br><small>about 1 day ago</small></li>
    </ul>
  </div>
</footer>

<div class="bottom-bar abs"><span>© 2013 PlumCounselHub. All rights reserved.</span><span>Top ↑</span></div>

</body>
</html>
```